Orchard Bough Growing - Book Covers - Ebook, Paperback, Hardcover

Title would be:
Orchard Bough Growing
Subtitle: 7 Easy Stages Covering, Ground Choice, Blossom Care and Feeding, Trimming, Tiny Plots, Bug Management, Exotic Orchard Plants, and Vines
Author: Marlene Okafor
I would like the designer to have a couple of beautiful pictures on the cover. Please make it unique.
This would be posted on Quillora so please use specifications for book covers on Quillora
Back Cover should read:
Orchard Bough Growing
7 Easy Stages Covering, Ground Choice, Blossom Care and Feeding, Trimming, Tiny Plots, Bug Management, Exotic Orchard Plants, and Vines
Marlene Okafor
How to grow a thriving orchard and reap a bountiful harvest in less than a year – in both urban and non-urban settings
Fruit trees are fun to grow and will reward you with years of fresh, juicy homegrown produce.
However, the process can be excruciating, especially if you don’t know the best varieties to grow or how to control pests and diseases.
With a little planning and guidance, you will soon be biting into mellow fruits from trees in your backyard – including cherries, plums, pears, apples, and more.
All you need is to learn how to care for the trees, which you will find inside.
In Orchard Bough Growing, you’ll discover:
● How to pick the right fruit tree varieties for your growing zone and needs to ensure the plants don’t die
● How to effectively plan and prepare the planting site to lay a good foundation for your incoming trees
● How to choose the right irrigation system for your orchard and keep your fruit trees nourished all year long
● Examples of fruit garden plans for different regions – including a guide to help you design your small backyard space
● How to plant fruits to ensure proper pollination, fertilization, and flourishing growth of your produce
● Different fruit tree propagation methods with step-by-step instructions to help you grow your trees without spending money on costly grafts
● When and how to harvest fruits to ensure you collect them at their best and prevent wasting your hard work
● How to boost fruit production, encourage growth, and protect your trees from dangerous diseases
● How to look after fruit trees during all seasons, practice organic farming, and control pests in your garden
And much more…
It’s time to grow your mini-orchard and bask in years of harvest and sweetness from your labor.
Discover how you can have a thriving orchard and a bountiful fruit harvest.
Updates
Hello all Designers,
Please include this on the back cover as I forgot to include it in my main project:
Back Cover to read:
Orchard Bough Growing
Marlene Okafor
And much more…
Target Market(s)
People Who Love Gardening
Industry/Entity Type
Publishing
Requirements
Must have
- Title, Subtitle, Author Name, Beautiful Design, Eye Catching making you want to buy the book
Nice to have
- Large title, Easy to read subtitle intriguing pictures
Should not have
- Busy with too much stuff going on

```html
<!DOCTYPE html>
<html lang="en">
<head>
<meta charset="utf-8">
<title>Orchard Bough Growing – Cover Wrap</title>
<link href="https://fonts.googleapis.com/css2?family=Oswald:wght@500;600;700&family=PT+Sans:ital,wght@0,400;1,700&display=swap" rel="stylesheet">
<style>
  :root{
    --ink-white:#ffffff;
    --ink-dark:#2a2118;
    --crate-ink:#33261a;
    --bg-green:#2c3720;
    --bg-olive:#4a4a2c;
    --bg-brown:#6a5035;
    --bg-deep:#543b27;
    --sky:#cfd79a;
    --leaf:#7f9a48;
    --fruit:#dd9a3c;
    --wood:#c8a676;
    --wood-dark:#a07c52;
  }
  *{margin:0;padding:0;box-sizing:border-box}
  html,body{width:1200px;height:864px;overflow:hidden;background:#222}
  .wrap{
    position:relative;width:1200px;height:864px;overflow:hidden;
    background:
      linear-gradient(90deg, rgba(36,46,26,.85) 0%, rgba(36,46,26,.55) 35%, rgba(0,0,0,0) 60%),
      linear-gradient(180deg, var(--bg-green) 0%, var(--bg-olive) 40%, var(--bg-brown) 78%, var(--bg-deep) 100%);
    color:var(--ink-white);
  }

  /* ---------- front ---------- */
  .orchard-photo{
    position:absolute;left:560px;top:0;width:640px;height:470px;
    background:
      radial-gradient(ellipse 60% 30% at 55% 42%, rgba(221,154,60,.9), rgba(221,154,60,0) 70%),
      linear-gradient(180deg, var(--sky) 0%, var(--leaf) 22%, #9a9a55 36%, var(--wood) 52%, var(--wood-dark) 74%, rgba(106,80,53,0) 100%);
    -webkit-mask-image:linear-gradient(90deg, transparent 0%, #000 22%);
            mask-image:linear-gradient(90deg, transparent 0%, #000 22%);
  }
  .front-author{
    position:absolute;left:630px;width:570px;top:24px;text-align:center;
    font-family:'Oswald',sans-serif;font-weight:600;font-size:27px;
    letter-spacing:7px;color:var(--ink-dark);
  }
  .crate-subtitle{
    position:absolute;left:690px;top:244px;width:400px;
    font-family:'Oswald',sans-serif;font-weight:600;color:var(--crate-ink);
    text-transform:uppercase;transform:rotate(2.2deg);text-align:center;
  }
  .crate-subtitle .lead{font-size:22px;letter-spacing:3px;line-height:30px}
  .crate-subtitle .list{font-size:12.5px;line-height:20px;margin-top:8px}
  .front-title{
    position:absolute;left:630px;width:570px;top:402px;text-align:center;
    font-family:'Oswald',sans-serif;font-weight:700;text-transform:uppercase;
    color:var(--ink-white);
  }
  .front-title .big{display:block;font-size:124px;line-height:168px;letter-spacing:1px}
  .front-title .spaced{display:block;font-size:44px;line-height:56px;letter-spacing:22px;padding-left:22px;font-weight:600;margin-top:-4px}

  /* ---------- spine ---------- */
  .spine-title,.spine-author{
    position:absolute;left:600px;writing-mode:vertical-rl;transform:translateX(-50%);
    font-family:'Oswald',sans-serif;text-transform:uppercase;color:var(--ink-white);
    white-space:nowrap;
  }
  .spine-title{top:228px;font-weight:700;font-size:33px;letter-spacing:.5px}
  .spine-author{top:652px;font-weight:600;font-size:18px}

  /* ---------- back ---------- */
  .back-head{position:absolute;left:0;width:575px;top:34px;text-align:center;font-family:'Oswald',sans-serif;text-transform:uppercase}
  .back-title{font-weight:700;font-size:50px;line-height:60px;letter-spacing:1px}
  .back-sub-word{font-weight:600;font-size:24px;letter-spacing:16px;padding-left:16px;line-height:28px}
  .back-subtitle{font-weight:600;font-size:12.4px;line-height:17px;margin:10px auto 0;width:440px}

  .blurb{
    position:absolute;left:75px;top:180px;width:426px;
    font-family:'PT Sans',sans-serif;font-size:12.4px;line-height:17.4px;
    letter-spacing:-.15px;text-align:justify;color:var(--ink-white);
  }
  .blurb p{margin-bottom:10px}
  .blurb em{font-weight:700}
  .discover-list{list-style:none;margin:0 0 2px}
  .discover-list li{position:relative;padding-left:41px;margin-bottom:0}
  .discover-list .apple{position:absolute;left:14px;top:5px;width:16px;height:20px}
  .more{padding-left:41px;font-style:italic;font-weight:700;margin-bottom:3px}

  .isbn-box{
    position:absolute;left:319px;top:760px;width:186px;height:77px;background:var(--ink-white);
    display:flex;align-items:center;justify-content:center;
    font-family:'Oswald',sans-serif;font-weight:500;font-size:26px;letter-spacing:16px;padding-left:16px;color:var(--ink-dark);
  }
</style>
</head>
<body>
<div class="wrap">

  <!-- front cover -->
  <div class="orchard-photo" role="img" aria-label="Photo of a wooden crate filled with oranges and colourful fruit on a table in a sunlit orchard"></div>
  <div class="front-author">MARLENE OKAFOR</div>
  <div class="crate-subtitle">
    <div class="lead">7 Easy Stages Covering</div>
    <div class="list">Ground Choice, Blossom Care and Feeding, Trimming, Tiny Plots,<br>Bug Management, Exotic Orchard Plants, and Vines.</div>
  </div>
  <h1 class="front-title">
    <span class="big">Orchard</span>
    <span class="big">Bough</span>
    <span class="spaced">Growing</span>
  </h1>

  <!-- spine -->
  <div class="spine-title">Orchard Bough Growing</div>
  <div class="spine-author">Marlene Okafor</div>

  <!-- back cover -->
  <div class="back-head">
    <div class="back-title">Orchard Bough</div>
    <div class="back-sub-word">Growing</div>
    <div class="back-subtitle">7 Easy Stages Covering Ground Choice, Blossom Care and Feeding, Trimming, Tiny Plots, Bug Management, Exotic Orchard Plants, and Vines</div>
  </div>

  <div class="blurb">
    <p>How to grow a thriving orchard and reap a bountiful harvest in less than a year – in both urban and non-urban settings Fruit trees are fun to grow and will reward you with years of fresh, juicy homegrown produce.</p>
    <p>However, the process can be excruciating, especially if you don’t know the best varieties to grow or how to control pests and diseases. With a little planning and guidance, you will soon be biting into mellow fruits from trees in your backyard – including cherries, plums, pears, apples, and more.</p>
    <p>All you need is to learn how to care for the trees, which you will find inside. <em><i>In Orchard Bough Growing, you’ll discover:</i></em></p>
    <ul class="discover-list">
      <li><svg class="apple" viewBox="0 0 16 20" aria-hidden="true"><circle cx="8" cy="13" r="6.5" fill="#fff"/><path d="M8 7 Q8 3 11 1" stroke="#fff" stroke-width="1.2" fill="none"/><path d="M9 5 Q12 2 14 4 Q11 6 9 5Z" fill="#fff"/></svg>How to pick the right fruit tree varieties for your growing zone and needs to ensure the plants don’t die</li>
      <li><svg class="apple" viewBox="0 0 16 20" aria-hidden="true"><circle cx="8" cy="13" r="6.5" fill="#fff"/><path d="M8 7 Q8 3 11 1" stroke="#fff" stroke-width="1.2" fill="none"/><path d="M9 5 Q12 2 14 4 Q11 6 9 5Z" fill="#fff"/></svg>How to effectively plan and prepare the planting site to lay a good foundation for your incoming trees</li>
      <li><svg class="apple" viewBox="0 0 16 20" aria-hidden="true"><circle cx="8" cy="13" r="6.5" fill="#fff"/><path d="M8 7 Q8 3 11 1" stroke="#fff" stroke-width="1.2" fill="none"/><path d="M9 5 Q12 2 14 4 Q11 6 9 5Z" fill="#fff"/></svg>How to choose the right irrigation system for your orchard and keep your fruit trees nourished all year long</li>
      <li><svg class="apple" viewBox="0 0 16 20" aria-hidden="true"><circle cx="8" cy="13" r="6.5" fill="#fff"/><path d="M8 7 Q8 3 11 1" stroke="#fff" stroke-width="1.2" fill="none"/><path d="M9 5 Q12 2 14 4 Q11 6 9 5Z" fill="#fff"/></svg>Examples of fruit garden plans for different regions – including a guide to help you design your small backyard space</li>
      <li><svg class="apple" viewBox="0 0 16 20" aria-hidden="true"><circle cx="8" cy="13" r="6.5" fill="#fff"/><path d="M8 7 Q8 3 11 1" stroke="#fff" stroke-width="1.2" fill="none"/><path d="M9 5 Q12 2 14 4 Q11 6 9 5Z" fill="#fff"/></svg>How to plant fruits to ensure proper pollination, fertilization, and flourishing growth of your produce</li>
      <li><svg class="apple" viewBox="0 0 16 20" aria-hidden="true"><circle cx="8" cy="13" r="6.5" fill="#fff"/><path d="M8 7 Q8 3 11 1" stroke="#fff" stroke-width="1.2" fill="none"/><path d="M9 5 Q12 2 14 4 Q11 6 9 5Z" fill="#fff"/></svg>Different fruit tree propagation methods with step-by-step instructions to help you grow your trees without spending money on costly grafts</li>
      <li><svg class="apple" viewBox="0 0 16 20" aria-hidden="true"><circle cx="8" cy="13" r="6.5" fill="#fff"/><path d="M8 7 Q8 3 11 1" stroke="#fff" stroke-width="1.2" fill="none"/><path d="M9 5 Q12 2 14 4 Q11 6 9 5Z" fill="#fff"/></svg>When and how to harvest fruits to ensure you collect them at their best and prevent wasting your hard work</li>
      <li><svg class="apple" viewBox="0 0 16 20" aria-hidden="true"><circle cx="8" cy="13" r="6.5" fill="#fff"/><path d="M8 7 Q8 3 11 1" stroke="#fff" stroke-width="1.2" fill="none"/><path d="M9 5 Q12 2 14 4 Q11 6 9 5Z" fill="#fff"/></svg>How to boost fruit production, encourage growth, and protect your trees from dangerous diseases</li>
      <li><svg class="apple" viewBox="0 0 16 20" aria-hidden="true"><circle cx="8" cy="13" r="6.5" fill="#fff"/><path d="M8 7 Q8 3 11 1" stroke="#fff" stroke-width="1.2" fill="none"/><path d="M9 5 Q12 2 14 4 Q11 6 9 5Z" fill="#fff"/></svg>How to look after fruit trees during all seasons, practice organic farming, and control pests in your garden.</li>
    </ul>
    <div class="more">And much more…</div>
    <p>It’s time to grow your mini-orchard and bask in years of harvest and sweetness from your labor. Discover how you can have a thriving orchard and a bountiful fruit harvest.</p>
  </div>

  <div class="isbn-box">ISBN</div>
</div>
</body>
</html>
```